Christmas social media advert post

I am looking for an eye catching advert for use mainly on social media posts.
The following is the detail of the event.

Christmas special offer-
£10pp,– offer includes –
Half an hour Toboggan track,
Half an hour Slingshot paintballs (20 paintballs pp) and safe target archery (under cover and indoor ranges). Activities all the family from age 4 to grandparents can join in,
Also available – Add on indoor activities including Mini Curling, Bead Blitz, Safe axe throwing, Air juggler – from £3.50pp and age 6plus
Café open for hot food and drinks in the ‘Fireside Frost Lodge and the heated Christmas marquee.

A basic idea I put together for what I feel is the important information is -

Christmas Special offer -
Starts Saturday 20th December.
£10pp – offer includes –
Half an hour Slingshot paintballs (20 paintballs pp) and safe target archery (under cover and indoor ranges). Activities all the family from age 4 to grandparents can join in. Booking is essential - details on how below.
Also available Add on indoor activities - including Mini Curling, Bead Blitz, Safe axe throwing, Air juggler – from £3.50pp and age 6plus.
Ages start from 4 plus.
All activities are great for children and adults so perfect for families as well as friends, parties and get togethers.
Free huge car parks,
Booking is easy-
Just Message from messenger (on this post) or email
martin@hollowbrookleisurepark.co.uk for availability of your preferred date and time.

I would be happy to send the detailed information to enquiries if it meant a better looking advert / post.

Full details are in the picture uploads, feel free to use as much or as little of the information as you feel best.

```html
<!DOCTYPE html>
<html lang="en">
<head>
<meta charset="utf-8">
<title>Christmas Special Offer</title>
<link rel="stylesheet" href="https://fonts.googleapis.com/css2?family=Anton&family=Days+One&family=Montserrat:ital,wght@0,400;0,500;1,700;1,800&display=swap">
<style>
  :root {
    --white: #ffffff;
    --ink: #111111;
    --blue-deep: #1a3fb8;
    --blue-mid: #1f6fe0;
    --blue-sky: #2fa6e6;
    --blue-pale: #42b3ee;
    --red: #d40812;
    --red-dark: #7a0006;
    --photo-dark: #2b2f36;
    --photo-mid: #4a5140;
  }
  * { margin: 0; padding: 0; box-sizing: border-box; }
  html, body { width: 1200px; height: 1200px; overflow: hidden; background: var(--white); }
  .advert { position: relative; width: 1200px; height: 1200px; overflow: hidden; font-family: "Montserrat", sans-serif; color: var(--white); }
  .advert-art { position: absolute; inset: 0; }
  .headline-christmas {
    position: absolute; left: 0; width: 1200px; top: 72px; text-align: center;
    font-family: "Anton", sans-serif; font-size: 148px; line-height: 1; color: var(--ink); letter-spacing: 1px;
    padding-right: 80px;
  }
  .headline-special {
    position: absolute; left: 180px; top: 262px;
    font-family: "Days One", sans-serif; font-size: 118px; line-height: 1; color: var(--white);
    transform: rotate(-4deg); transform-origin: left bottom;
  }
  .headline-offer {
    position: absolute; left: 662px; top: 332px;
    font-family: "Days One", sans-serif; font-size: 112px; line-height: 1; color: var(--white);
    transform: rotate(-17deg); transform-origin: center center;
  }
  .price {
    position: absolute; left: 1015px; top: 574px; transform: translateX(-50%);
    font-family: "Montserrat", sans-serif; font-weight: 800; font-size: 60px; line-height: 1;
  }
  .offer-title {
    position: absolute; left: 70px; top: 615px;
    font-weight: 800; font-style: italic; font-size: 48px; line-height: 1.25; text-transform: uppercase;
  }
  .family-note { position: absolute; left: 70px; top: 780px; font-size: 22px; line-height: 1.45; }
  .family-note strong { font-weight: 700; font-style: italic; }
  .small-note { position: absolute; left: 70px; font-size: 17px; line-height: 1.55; }
  .addons { top: 880px; }
  .cafe { top: 950px; }
  .included-list {
    position: absolute; right: 80px; top: 698px; text-align: right;
    font-size: 20px; line-height: 1.4; font-weight: 400;
  }
  .included-list p + p { margin-top: 20px; }
</style>
</head>
<body>
<main class="advert">
  <svg class="advert-art" width="1200" height="1200" viewBox="0 0 1200 1200">
    <defs>
      <linearGradient id="bgBlue" x1="0" y1="0" x2="1" y2="0.3">
        <stop offset="0" stop-color="var(--blue-deep)"/>
        <stop offset="0.55" stop-color="var(--blue-mid)"/>
        <stop offset="1" stop-color="var(--blue-sky)"/>
      </linearGradient>
      <linearGradient id="bannerBlue" x1="0" y1="0" x2="1" y2="0">
        <stop offset="0" stop-color="var(--blue-pale)"/>
        <stop offset="1" stop-color="var(--blue-deep)"/>
      </linearGradient>
      <linearGradient id="bannerRed" x1="0" y1="1" x2="1" y2="0">
        <stop offset="0" stop-color="var(--red-dark)"/>
        <stop offset="0.6" stop-color="var(--red)"/>
      </linearGradient>
      <linearGradient id="priceRed" x1="0" y1="0" x2="1" y2="0">
        <stop offset="0" stop-color="var(--red-dark)"/>
        <stop offset="0.5" stop-color="var(--red)"/>
      </linearGradient>
      <linearGradient id="photoTone" x1="0" y1="0" x2="1" y2="1">
        <stop offset="0" stop-color="var(--photo-mid)"/>
        <stop offset="1" stop-color="var(--photo-dark)"/>
      </linearGradient>
    </defs>
    <rect class="bg-blue" width="1200" height="1200" fill="url(#bgBlue)"/>
    <path class="chevron" d="M600,660 L800,660 L920,780 L800,900 L600,900 L720,780 Z" fill="var(--blue-pale)" opacity="0.25"/>
    <path class="price-band" d="M740,560 C900,540 1060,500 1200,468 V668 C1080,660 900,620 740,560 Z" fill="url(#priceRed)"/>
    <path class="top-white" d="M0,0 H1200 V432 C1050,470 880,580 640,585 C420,590 200,500 0,405 Z" fill="var(--white)"/>
    <path class="banner-blue" d="M58,346 Q480,180 964,201 L900,440 Q600,480 185,473 Z" fill="url(#bannerBlue)"/>
    <path class="banner-red" d="M415,427 Q720,330 964,201 L1200,452 Q1020,468 840,505 Q620,505 415,427 Z" fill="url(#bannerRed)"/>
    <path class="photo-area" role="img" aria-label="Photo of a child aiming a slingshot at targets in a camouflage-netted indoor range"
      d="M227,1200 C260,1080 380,1000 560,968 C800,935 1050,960 1200,1000 V1200 Z" fill="url(#photoTone)"/>
  </svg>

  <h1 class="headline-christmas">Christmas</h1>
  <div class="headline-special">special</div>
  <div class="headline-offer">offer</div>
  <div class="price">£10pp</div>

  <h2 class="offer-title">Half an hour<br>Toboggan track</h2>

  <p class="family-note">Activities all the family from<br><strong>age 4 to grandparents can join in</strong></p>

  <p class="small-note addons">Add on indoor activities including Mini Curling, Bead Blitz,<br>Safe axe throwing, Air juggler – from £3.50pp and age 6plus</p>

  <p class="small-note cafe">Café open for hot food and drinks in the ‘Fireside Frost<br>Lodge and the heated Christmas marquee.</p>

  <div class="included-list">
    <p>Half an hour Slingshot paintballs<br>(20 paintballs pp)</p>
    <p>safe target archery<br>(under cover and indoor ranges).</p>
  </div>
</main>
</body>
</html>
```